Web Site design for Computer Security Company

Would like a "web 2.0", parralax style website created for a internet security company called "BrindleCove". Really like the way a website like quorimesh.example looks. Like to have 3 steps like they do to explain our product/service.

1# Identify #2Analyze #3Educate

Would like the website to expand with additional information if they click on any of the items 1-3.

Have attached a logo to get an idea of colors. Would like a clean white background.

Pages: (could be one long page or individual pages, I'm open to ideas)

Home
About Us
Services
Contact us

Theme ideas: Research, Security, Lab, Education

Do not want a dark site with typical hacker images etc. Would like to portray the image that we are experts, and we will work with our customers to identify their risk areas on the internet, then train their users around security awareness.

Target Market(s)

Financial

Industry/Entity Type

Computer Security

Coding

Number of Pages Required

4 page

Font styles to use
Sans Serif

Colors
33a6d7
0555a3
9bcb3b
ffffff

Requirements
Must have
• Clean web2.0 look.
• White background
• Threat, security, education, R&D are themes.
• working with logo to integrate a common color scheme.
• design feel like quorimesh.example
Nice to have
• Parralax or similar style page that expands for certain areas.
Should not have
• must not be black/dark with hacker images

```html
<!DOCTYPE html>
<html lang="en">
<head>
<meta charset="utf-8">
<title>BrindleCove — Secure Your People</title>
<link href="https://fonts.googleapis.com/css2?family=Raleway:wght@400;500;600;700&family=Open+Sans:wght@400;600&display=swap" rel="stylesheet">
<style>
:root{
  --blue:#33a6d7;
  --navy:#0555a3;
  --green:#9bcb3b;
  --white:#ffffff;
  --ink:#2b3a48;
  --text:#3d4650;
  --mist:#eef3f7;
  --line:#d5dbe0;
  --field:#dfe3e6;
}
*{box-sizing:border-box;margin:0;padding:0}
html,body{width:1200px;height:2990px;overflow:hidden}
body{position:relative;background:var(--white);font-family:"Open Sans",Arial,sans-serif;color:var(--text)}
.abs{position:absolute}
h1,h2,h3,.nav a,.brand-name{font-family:"Raleway",Arial,sans-serif}

/* header */
.site-header{left:0;top:0;width:1200px;height:134px;background:linear-gradient(#ffffff,#f1f3f4);border-bottom:3px solid var(--navy)}
.brand{left:160px;top:12px;width:200px;text-align:center}
.brand-mark{width:56px;height:56px;border-radius:50%;border:3px solid var(--blue);margin:0 auto 4px}
.brand-name{font-size:26px;font-weight:700;color:var(--ink);line-height:30px}
.brand-tag{font-size:9px;letter-spacing:1px;color:var(--ink)}
.call{right:160px;top:32px;font-family:"Raleway",sans-serif;font-size:16px;font-weight:600;color:var(--blue)}
.nav{right:160px;top:88px;display:flex;gap:48px}
.nav a{font-size:13px;font-weight:600;color:var(--ink);text-decoration:none}
.nav a.active{color:var(--blue)}

/* hero */
.hero{left:0;top:134px;width:1200px;height:580px;background:linear-gradient(#0f8fdf,#3cbdcb)}
.hero h1{left:160px;top:176px;font-size:38px;font-weight:500;color:var(--white)}
.hero p{left:160px;top:238px;width:420px;font-size:13px;line-height:20px;color:var(--white)}
.btn-outline{left:162px;top:328px;width:154px;height:44px;border:2px solid var(--white);color:var(--white);font-family:"Raleway",sans-serif;font-size:12px;font-weight:700;line-height:40px;text-align:center}
.hero-art{left:600px;top:0;width:600px;height:500px;background:radial-gradient(circle at 60% 45%,rgba(255,255,255,.28),rgba(255,255,255,0) 70%)}

/* steps */
.section-title{width:1200px;left:0;text-align:center;font-size:29px;font-weight:600;color:var(--ink)}
.section-lead{left:0;width:1200px;text-align:center;font-size:11px;color:var(--text)}
.step-wave{left:0;top:880px}
.step{width:260px;text-align:center}
.step h3{font-size:19px;font-weight:600;color:var(--ink);margin-bottom:18px}
.step p{font-size:11px;line-height:22px;color:var(--text);padding:0 18px}

/* about */
.about{left:0;top:1248px;width:1200px;height:772px;background:var(--mist);border-top:1px solid var(--line)}
.about-intro{left:170px;top:130px;width:860px;text-align:center;font-size:11px;line-height:22px}
.col{width:426px}
.col h3{font-size:17px;font-weight:500;color:var(--blue);line-height:24px;margin-bottom:30px}
.col p{font-size:11px;line-height:22px;margin-bottom:18px}
.btn-green{display:block;margin-top:46px;width:108px;height:40px;background:var(--green);color:var(--white);font-family:"Raleway",sans-serif;font-size:12px;font-weight:600;line-height:40px;text-align:center}

/* contact */
.field{height:36px;background:var(--white);border:1px solid var(--field);font-size:11px;color:var(--text);padding:10px 6px}
.field.select::after{content:"";position:absolute;right:0;top:0;width:34px;height:34px;border-left:1px solid var(--field)}
.caret{right:12px;top:13px;width:8px;height:8px}
.btn-blue{left:162px;top:2432px;width:92px;height:40px;background:var(--blue);color:var(--white);font-family:"Raleway",sans-serif;font-weight:700;font-size:13px;line-height:40px;text-align:center}
.info-icon{width:38px;height:38px;border-radius:50%;border:2px solid var(--blue);display:flex;align-items:center;justify-content:center}
.info-text{font-size:11px;line-height:20px;color:var(--ink)}

/* map & footer */
.map{left:0;top:2550px;width:1200px;height:270px;background:linear-gradient(135deg,#d4d5d6,#e6e6e6 50%,#cfd0d1)}
.site-footer{left:0;top:2820px;width:1200px;height:170px;background:var(--mist)}
.social{left:506px;top:36px;display:flex;gap:12px}
.social span{width:40px;height:40px;border-radius:50%;border:2px solid var(--green)}
.foot-nav{left:0;width:1200px;top:100px;text-align:center;font-family:"Raleway",sans-serif;font-size:11px;font-weight:700;color:var(--ink);word-spacing:2px}
.foot-nav i{font-style:normal;margin:0 22px}
.copy{left:0;width:1200px;top:138px;text-align:center;font-size:11px;color:var(--ink)}
</style>
</head>
<body>

<header class="site-header abs">
  <div class="brand abs">
    <div class="brand-mark"></div>
    <div class="brand-name">BrindleCove</div>
    <div class="brand-tag">SECURE YOUR PEOPLE</div>
  </div>
  <div class="call abs">CALL US NOW: (020) 555-0142</div>
  <nav class="nav abs">
    <a class="active" href="#">HOME</a><a href="#">SERVICES</a><a href="#">ABOUT US</a><a href="#">CONTACT US</a>
  </nav>
</header>

<section class="hero abs">
  <h1 class="abs">Secure Your People</h1>
  <p class="abs">Sed ut perspiciatis unde omnis iste natus error sit voluptatem accusantium doloremque laudantium, totam rem aperiam, eaque ipsa quae ab illo inventore veritatis et quasi architecto beatae vitae dicta sun.</p>
  <div class="btn-outline abs">GET STARTED HERE</div>
  <div class="hero-art abs" role="img" aria-label="Illustration of an analyst at a desk computer linked to a network of people in circles"></div>
</section>

<h2 class="section-title abs" style="top:774px">3 Steps Process to Explain Our Service</h2>
<p class="section-lead abs" style="top:822px">Sed ut perspiciatis unde omnis iste natus error sit voluptatem accusantium doloremque laudantium, totam rem aperiam.</p>

<svg class="step-wave abs" width="1200" height="130" viewBox="0 0 1200 130">
  <path d="M40 80 C120 100 180 60 296 60 C380 60 400 100 444 95 C500 90 520 60 594 60 C680 60 710 100 760 95 C820 90 840 60 910 60 C1030 60 1080 100 1160 80" fill="none" stroke="#cfd4d8" stroke-width="2"/>
  <g fill="#fff" stroke-width="6">
    <circle cx="296" cy="60" r="56" stroke="#33a6d7"/>
    <circle cx="444" cy="82" r="22" stroke="#9bcb3b"/>
    <circle cx="594" cy="60" r="56" stroke="#33a6d7"/>
    <circle cx="760" cy="82" r="22" stroke="#9bcb3b"/>
    <circle cx="910" cy="60" r="56" stroke="#33a6d7"/>
  </g>
  <g fill="none" stroke="#9bcb3b" stroke-width="4">
    <rect x="274" y="38" width="26" height="30"/>
    <circle cx="306" cy="66" r="11" stroke="#33a6d7"/>
    <line x1="314" y1="74" x2="324" y2="84" stroke="#33a6d7" stroke-width="5"/>
    <rect x="576" y="36" width="28" height="38"/>
    <line x1="582" y1="46" x2="598" y2="46"/><line x1="582" y1="54" x2="594" y2="54"/>
    <circle cx="606" cy="70" r="9" stroke="#33a6d7"/>
    <line x1="613" y1="77" x2="620" y2="84" stroke="#33a6d7" stroke-width="5"/>
  </g>
  <g fill="#9bcb3b">
    <polygon points="910,40 940,54 910,68 880,54"/>
    <rect x="896" y="60" width="28" height="14"/>
    <rect x="936" y="54" width="3" height="20"/>
  </g>
</svg>

<div class="step abs" style="left:166px;top:1024px"><h3>1# Identify</h3><p>BrindleCove has developed industry leading software that will intelligently build a profile of a company's attack surface. This is the first step to identify and evaluate todays internet based risk and attacks. The attack surface includes.</p></div>
<div class="step abs" style="left:464px;top:1024px"><h3>2# Analyze</h3><p>One the attack surface has been realized, the BrindleCove analytics engine(s) is used to further identify relationships between employees and social media, along with other forums and web-sites. This data is fed into passive.</p></div>
<div class="step abs" style="left:780px;top:1024px"><h3>3# Educate</h3><p>After the attack surface has been mapped out, and security assessments have been peformed, BrindleCove provides an in-depth series of online training material. This material is custom designed for each client and relevant to their.</p></div>

<section class="about abs">
  <h2 class="section-title abs" style="top:68px">About us</h2>
  <p class="about-intro abs">BrindleCove is a leader in Social Engineering and Security awareness education. Our cutting-edge analytics software is a first of its kind to truly identify an organizations attack surface to provide realistic assessments that identify users overall security awareness level. This is follow-up with custom tailored training material that not only has been designed for individual markets, but also specific regulations. This ensures that all users have been trained to help limit risk and exposure for an organization.</p>
  <div class="col abs" style="left:162px;top:244px">
    <h3>Sed ut perspiciatis unde omnis iste natus error sit volu ptatem accusantium doloremque laudantium.</h3>
    <p>Sed ut perspiciatis unde omnis iste natus error sit voluptatem accusantium doloremque laudantium, totam rem aperiam, eaque ipsa quae ab illo inventore veritatis et quasi architecto beatae vitae dicta sunt explicabo. Nemo enim ipsam voluptatem quia voluptas sit aspernatur aut od.</p>
    <p>Sed ut perspiciatis unde omnis iste natus error sit voluptatem accusantium doloremque laudantium, totam rem aperiam, eaque ipsa quae ab illo inventore veritatis et quasi architecto beatae vitae dicta sunt explicabo. Nemo enim ipsam voluptatem quia voluptas sit aspernatur aut od.</p>
    <span class="btn-green">READ MORE</span>
  </div>
  <div class="col abs" style="left:632px;top:244px">
    <h3>Sed ut perspiciatis unde omnis iste natus error sit volu ptatem accusantium doloremque laudantium.</h3>
    <p>Sed ut perspiciatis unde omnis iste natus error sit voluptatem accusantium doloremque laudantium, totam rem aperiam, eaque ipsa quae ab illo inventore veritatis et quasi architecto beatae vitae dicta sunt explicabo. Nemo enim ipsam voluptatem quia voluptas sit aspernatur aut od.</p>
    <p>Sed ut perspiciatis unde omnis iste natus error sit voluptatem accusantium doloremque laudantium, totam rem aperiam, eaque ipsa quae ab illo inventore veritatis et quasi architecto beatae vitae dicta sunt explicabo. Nemo enim ipsam voluptatem quia voluptas sit aspernatur aut od.</p>
    <span class="btn-green">READ MORE</span>
  </div>
  <svg class="abs" style="left:0;top:650px" width="1200" height="80" viewBox="0 0 1200 80">
    <path d="M40 48 C140 70 200 32 285 32 C380 32 440 70 520 60 C570 54 570 32 594 32 C680 32 720 70 800 60 C860 52 870 32 906 32 C1000 32 1080 70 1160 48" fill="none" stroke="#cdd3d8" stroke-width="2"/>
    <g fill="#fff" stroke="#9bcb3b" stroke-width="2"><circle cx="285" cy="32" r="7"/><circle cx="594" cy="32" r="7"/><circle cx="906" cy="32" r="7"/></g>
  </svg>
</section>

<h2 class="section-title abs" style="top:2066px">Contact Us</h2>
<p class="section-lead abs" style="top:2122px;left:240px;width:720px;line-height:22px">Sed ut perspiciatis unde omnis iste natus error sit voluptatem accusantium doloremque laudantium, totam rem aperiam, eaque ipsa quae ab illo inventore veritatis et quasi architecto beatae vitae dicta sunt explicabo. Nemo enim ipsam voluptatem quia voluptas sit aspernatur aut od.</p>

<form>
  <div class="field abs" style="left:162px;top:2196px;width:284px">Name:</div>
  <div class="field abs" style="left:456px;top:2196px;width:286px">Email:</div>
  <div class="field abs" style="left:162px;top:2240px;width:284px">Phone:</div>
  <div class="field select abs" style="left:456px;top:2240px;width:286px">More info:<svg class="caret abs" viewBox="0 0 8 8"><path d="M1 2l3 4 3-4" fill="none" stroke="#777"/></svg></div>
  <div class="field select abs" style="left:162px;top:2284px;width:284px">sales<svg class="caret abs" viewBox="0 0 8 8"><path d="M1 2l3 4 3-4" fill="none" stroke="#777"/></svg></div>
  <div class="field select abs" style="left:456px;top:2284px;width:286px">Schedule a call<svg class="caret abs" viewBox="0 0 8 8"><path d="M1 2l3 4 3-4" fill="none" stroke="#777"/></svg></div>
  <div class="field abs" style="left:162px;top:2330px;width:580px;height:90px">Message:</div>
  <div class="btn-blue abs">SUBMIT</div>
</form>

<div class="info-icon abs" style="left:808px;top:2218px"><svg width="14" height="18" viewBox="0 0 14 18"><path d="M7 17C3 11 1 8.5 1 6a6 6 0 0 1 12 0c0 2.5-2 5-6 11z" fill="none" stroke="#33a6d7" stroke-width="2"/><circle cx="7" cy="6" r="2" fill="#33a6d7"/></svg></div>
<div class="info-text abs" style="left:862px;top:2216px;width:150px">Lorem ipsum dolorsit amet, cons adipisicing elit, sed do eiu.</div>
<div class="info-icon abs" style="left:808px;top:2286px"><svg width="16" height="16" viewBox="0 0 16 16"><path d="M3 1l3 3-2 2c1 2.5 3.5 5 6 6l2-2 3 3-2 2C7 15 1 9 1 3z" fill="#33a6d7"/></svg></div>
<div class="info-text abs" style="left:862px;top:2282px">Phone:+01 555 0198 3327<br>Fax: 02 5550 1184</div>
<div class="info-icon abs" style="left:808px;top:2352px"><svg width="16" height="12" viewBox="0 0 16 12"><rect x="1" y="1" width="14" height="10" fill="none" stroke="#33a6d7" stroke-width="2"/><path d="M1 1l7 6 7-6" fill="none" stroke="#33a6d7" stroke-width="2"/></svg></div>
<div class="info-text abs" style="left:862px;top:2346px">hello@brindlecove.example<br>help@brindlecove.example</div>

<div class="map abs" role="img" aria-label="Street map of the office neighbourhood with a green location pin"></div>

<footer class="site-footer abs">
  <div class="social abs"><span></span><span></span><span></span><span></span></div>
  <div class="foot-nav abs">HOME<i>//</i>SERVICES<i>//</i>ABOUT US<i>//</i>CONTACT US</div>
  <div class="copy abs">© 2016 BrindleCove. All Copyrights are Reserved. Terms of Use &nbsp; Privacy Policy &nbsp; Sitemap &nbsp; Contact Us</div>
</footer>

</body>
</html>
```